Collaborative Law Bus Stop Bench Design

We are looking for a design for a bus stop bench-the size is 74 inches in length and 22 inches wide.We are a group of family law lawyers, social workers and accountants who are committed to resolving marital breakdowns without going to court.
As this is a bus stop ad not a lot of words can be used.
The sign needs to show our website www.tidewellhomecounsel.com prominently
We want the design to focus on the advantages of our process ie. not going to court-like"Don't air your dirty laundry"-a design with a clothesline or something like that.
It needs to be clear and uncomplicated but memorable.

```html
<!DOCTYPE html>
<html lang="en">
<head>
<meta charset="utf-8">
<title>Tidewell Home Counsel – Bus Stop Bench</title>
<link rel="stylesheet" href="https://fonts.googleapis.com/css2?family=Arvo:wght@700&family=Archivo+Black&family=Kaushan+Script&family=Tinos:wght@700&display=swap">
<style>
  :root {
    --wall-light: #c9b596;
    --wall-mid: #8a6f52;
    --ground-dark: #3a2a1e;
    --card: #ffffff;
    --sign-ink: #2a1212;
    --tag-blue: #1f5fb0;
    --tag-red: #d0202a;
    --web-red: #d4141e;
    --web-outline: #1a0505;
  }
  * { margin: 0; padding: 0; box-sizing: border-box; }
  html, body { width: 1200px; height: 374px; overflow: hidden; background: #000; }
  .bench-ad {
    position: relative;
    width: 1200px;
    height: 374px;
    overflow: hidden;
  }
  .scene-photo {
    position: absolute; inset: 0;
    background:
      radial-gradient(ellipse at 55% 10%, rgba(230,215,185,0.55), transparent 60%),
      linear-gradient(180deg, var(--wall-light) 0%, var(--wall-mid) 45%, #5b4532 75%, var(--ground-dark) 100%);
  }
  .sign {
    position: absolute;
    background: var(--card);
    display: flex; align-items: center; justify-content: center;
    box-shadow: 2px 3px 6px rgba(0,0,0,0.35);
  }
  .word {
    font-family: "Arvo", "Rockwell", serif;
    font-weight: 700;
    color: var(--sign-ink);
    line-height: 1;
    white-space: nowrap;
  }
  .sign--dont   { left: 176px; top: 22px;  width: 162px; height: 92px;  transform: rotate(-8deg); }
  .sign--air    { left: 352px; top: 42px;  width: 104px; height: 90px;  transform: rotate(-32deg) skewX(14deg); }
  .sign--air .word { transform: skewX(-14deg) rotate(12deg); }
  .sign--your   { left: 552px; top: 58px;  width: 138px; height: 76px;  transform: rotate(-9deg); }
  .sign--dirty  { left: 740px; top: 38px;  width: 150px; height: 96px;  transform: rotate(-2deg); }
  .sign--laundry{ left: 906px; top: 40px;  width: 152px; height: 78px;  transform: rotate(-16deg); }
  .sign--dont .word, .sign--dirty .word { font-size: 40px; }
  .sign--air .word  { font-size: 42px; }
  .sign--your .word { font-size: 38px; }
  .sign--laundry .word { font-size: 30px; }

  .tag {
    position: absolute;
    background: var(--card);
    display: flex; flex-direction: column; align-items: center; justify-content: center;
    box-shadow: 2px 3px 6px rgba(0,0,0,0.35);
    line-height: 1;
  }
  .tag__script {
    font-family: "Kaushan Script", cursive;
    font-size: 24px;
  }
  .tag__caps {
    font-family: "Archivo Black", sans-serif;
    color: var(--tag-blue);
    letter-spacing: 1px;
  }
  .tag--court    { left: 124px; top: 202px; width: 130px; height: 94px; transform: rotate(-8deg); }
  .tag--court .tag__script { color: var(--tag-blue); margin-left: -30px; }
  .tag--court .tag__caps { font-size: 30px; margin-top: 4px; }
  .tag--conflict { left: 504px; top: 186px; width: 132px; height: 84px; transform: rotate(-4deg); }
  .tag--conflict .tag__script { color: var(--tag-blue); font-size: 22px; }
  .tag--conflict .tag__caps { font-size: 22px; margin-top: 6px; }
  .tag--trust    { left: 962px; top: 136px; width: 178px; height: 74px; transform: rotate(-5deg); }
  .tag--trust .tag__script { color: var(--tag-red); margin-left: 30px; }
  .tag--trust .tag__caps { font-size: 34px; margin-top: 2px; }

  .website {
    position: absolute;
    left: 250px; top: 300px;
    font-family: "Tinos", "Times New Roman", serif;
    font-weight: 700;
    font-size: 52px;
    color: var(--web-red);
    letter-spacing: 1px;
    -webkit-text-stroke: 1.5px var(--web-outline);
    text-shadow: 3px 3px 0 var(--web-outline);
    white-space: nowrap;
  }
</style>
</head>
<body>
<main class="bench-ad">
  <div class="scene-photo" role="img" aria-label="Photo of a group of people leaning against a wall, each holding a sign in front of their head"></div>

  <div class="sign sign--dont"><span class="word">"DON'T</span></div>
  <div class="sign sign--air"><span class="word">AIR</span></div>
  <div class="sign sign--your"><span class="word">YOUR</span></div>
  <div class="sign sign--dirty"><span class="word">DIRTY</span></div>
  <div class="sign sign--laundry"><span class="word">LAUNDRY"</span></div>

  <div class="tag tag--court"><span class="tag__script">Avoid</span><span class="tag__caps">COURT</span></div>
  <div class="tag tag--conflict"><span class="tag__script">Minimise</span><span class="tag__caps">CONFLICT</span></div>
  <div class="tag tag--trust"><span class="tag__script">Foster</span><span class="tag__caps">TRUST</span></div>

  <p class="website">www.tidewellhomecounsel.com</p>
</main>
</body>
</html>
```